Thai Restruant Business Card Design

A Business card design for a Thai and Laos take away restaurant.

We are a highly respectable take away restaurant in a small shopping center.

The design must have a Papaya Tree and Thai Palace.

The final design should communicate, innovation, fun and delicious food.

Industry/Entity Type

Restaurant

Contact Information for Business Card

Mango Hearth, Thai & Lao Food, Shop 4. 17 Elmsworth Lane. Harrowfield N.S.W 2190, Tel. 02-96417725, Open 7 Days From 8.30am To 6.30pm

```html
<!DOCTYPE html>
<html lang="en">
<head>
<meta charset="utf-8">
<title>Mango Hearth – Business Card</title>
<link rel="stylesheet" href="https://fonts.googleapis.com/css2?family=Open+Sans:wght@400;600&display=swap">
<style>
  :root {
    --page-bg: #e9e4dc;
    --card-green: #14a555;
    --card-green-deep: #0f8f49;
    --gold: #d9b95c;
    --gold-text: #e8c35a;
    --band-gold: #d8bb63;
    --white: #ffffff;
    --palace-gold: #c8a24a;
    --palace-stone: #e6e3da;
    --palace-sky: #b9c9d6;
  }
  html, body {
    margin: 0;
    width: 1200px;
    height: 1023px;
    overflow: hidden;
    background: var(--page-bg);
    font-family: "Open Sans", Arial, sans-serif;
  }
  .business-card {
    position: absolute;
    left: 150px;
    top: 254px;
    width: 900px;
    height: 515px;
    background: radial-gradient(ellipse at 40% 30%, var(--card-green) 0%, var(--card-green-deep) 100%);
    overflow: hidden;
    box-shadow: 0 8px 24px rgba(0,0,0,0.25);
    color: var(--white);
  }
  .brand {
    position: absolute;
    left: 70px;
    top: 62px;
    display: flex;
    align-items: center;
    gap: 18px;
  }
  .brand-dot {
    width: 40px;
    height: 40px;
    border-radius: 50%;
    background: var(--gold);
  }
  .brand-name {
    margin: 0;
    font-size: 64px;
    font-weight: 600;
    line-height: 1;
    color: var(--white);
  }
  .brand-descriptor {
    position: absolute;
    left: 128px;
    top: 142px;
    margin: 0;
    font-size: 24px;
    font-weight: 400;
    letter-spacing: 0.5px;
  }
  .contact {
    position: absolute;
    left: 90px;
    top: 210px;
    font-size: 21px;
    line-height: 1.3;
  }
  .contact p { margin: 0; }
  .contact .label { color: var(--gold-text); }
  .contact .hours-label { margin-top: 22px; }
  .contact .hours { font-size: 19px; }
  .contact .phone {
    display: flex;
    align-items: center;
    gap: 10px;
    font-size: 26px;
    margin-top: 2px;
  }
  .tagline-band {
    position: absolute;
    left: 0;
    right: 0;
    bottom: 0;
    height: 78px;
    background: var(--band-gold);
  }
  .tagline {
    position: absolute;
    left: 70px;
    bottom: 22px;
    margin: 0;
    font-size: 24px;
    color: rgba(255,255,255,0.92);
  }
  .palace-photo {
    position: absolute;
    right: 0;
    bottom: 0;
    width: 340px;
    height: 330px;
    background: linear-gradient(180deg, var(--palace-sky) 0%, var(--palace-gold) 40%, var(--palace-stone) 70%, var(--palace-gold) 100%);
  }
</style>
</head>
<body>
  <main class="business-card">
    <div class="brand">
      <span class="brand-dot"></span>
      <h1 class="brand-name">Mango Hearth</h1>
    </div>
    <p class="brand-descriptor">Thai and Laos Take Away Restaurant</p>

    <section class="contact">
      <p class="label">Mango Hearth, Thai &amp; Lao Food</p>
      <p>Shop 4. 17 Elmsworth Lane Harrowfield</p>
      <p>N.S.W 2190</p>
      <p class="label hours-label">Open Everyday</p>
      <p class="hours">9:00 am&nbsp; to&nbsp; 7:00pm</p>
      <p class="phone">
        <svg width="24" height="20" viewBox="0 0 24 20" aria-hidden="true">
          <path d="M2 7 Q12 -1 22 7 L19 10 L16 7 L16 5 Q12 3.5 8 5 L8 7 L5 10 Z" fill="var(--gold-text)"/>
          <rect x="5" y="10" width="14" height="9" rx="2" fill="var(--gold-text)"/>
          <circle cx="12" cy="14.5" r="2.2" fill="var(--card-green)"/>
        </svg>
        <span>02-96417725</span>
      </p>
    </section>

    <div class="tagline-band"></div>
    <p class="tagline">We can insert tagline here</p>

    <div class="palace-photo" role="img" aria-label="Photograph of an ornate Thai royal palace with golden spired roofs"></div>
  </main>
</body>
</html>
```